Business Card Design for new consultancy company

Name of Company: Cobalt Wayline
Nature of Business: Digital Business Consultancy
Specialises in Digital Media Strategy, Digital Business Model Transformation, Over-The-Top (OTT) Development, Web Business Development, Digital Marketing, Web and App Product Development, Design and Innovation

Website: http://www.cobalt-wayline.example

Designs can be of any colour or any number of colours, objective is to give the impression we are a digital trend setter, creative and impactful.

Also please suggest a logo to complement the name and business card.

Target Market(s)

Media Companies, Telcos, Enterprises

Industry/Entity Type

Business

Contact Information for Business Card

Standard business card size. OK with to play with small variations like corners for impact/impression.

Font styles to use
Serif
Sans Serif

Requirements
Must have
• Clarity, Impact, Creativity
Nice to have
• Design should encapsulate professionalism, expertise, yet trend-setting and vibrant for digital consultancy
Should not have
• Messy layout, too gaudy colours or design

```html
<!DOCTYPE html>
<html lang="en">
<head>
<meta charset="utf-8">
<title>Cobalt Wayline – Business Card</title>
<link rel="stylesheet" href="https://fonts.googleapis.com/css2?family=Montserrat:wght@500;700&family=Arimo:wght@400&display=swap">
<style>
  :root {
    --page-bg: #ececec;
    --card-black: #05070c;
    --deep-navy: #0d1a33;
    --fiber-blue: #5f86c4;
    --fiber-light: #b9cdee;
    --accent-yellow: #f2e21a;
    --text-white: #ffffff;
  }
  * { margin: 0; padding: 0; box-sizing: border-box; }
  html, body {
    width: 1200px;
    height: 973px;
    overflow: hidden;
    background: var(--page-bg);
  }
  .card {
    position: absolute;
    left: 75px;
    top: 186px;
    width: 1050px;
    height: 600px;
    background: var(--card-black);
    overflow: hidden;
    box-shadow: 0 10px 30px rgba(0,0,0,0.18);
  }
  .card-visual {
    position: absolute;
    inset: 0;
    background:
      radial-gradient(ellipse 38% 52% at 58% 92%, rgba(70,105,170,0.75), rgba(20,35,70,0.6) 60%, transparent 100%),
      radial-gradient(ellipse 55% 60% at 18% 50%, var(--fiber-light) 0%, var(--fiber-blue) 35%, var(--deep-navy) 75%, transparent 100%),
      linear-gradient(90deg, var(--fiber-blue) 0%, var(--deep-navy) 45%, var(--card-black) 72%);
  }
  .card-content {
    position: absolute;
    left: 560px;
    top: 96px;
    color: var(--text-white);
  }
  .brand {
    display: flex;
    align-items: center;
    gap: 18px;
  }
  .brand-square {
    width: 56px;
    height: 56px;
    border: 3px solid var(--text-white);
  }
  .brand-name {
    font-family: "Montserrat", sans-serif;
    font-weight: 500;
    font-size: 40px;
    letter-spacing: 1px;
    color: var(--text-white);
    text-transform: uppercase;
    line-height: 1;
  }
  .person-name {
    margin-top: 34px;
    font-family: "Montserrat", sans-serif;
    font-weight: 700;
    font-size: 32px;
    letter-spacing: 4px;
    color: var(--accent-yellow);
    text-transform: uppercase;
  }
  .contact-list {
    list-style: none;
    margin-top: 22px;
    margin-left: 40px;
  }
  .contact-item {
    display: flex;
    align-items: center;
    gap: 14px;
    font-family: "Arimo", sans-serif;
    font-size: 23px;
    color: var(--text-white);
    margin-bottom: 16px;
  }
  .contact-icon { width: 26px; height: 26px; flex: none; }
</style>
</head>
<body>
  <div class="card">
    <div class="card-visual" role="img" aria-label="Photograph of glowing blue fibre-optic strands with a dark globe in the lower middle"></div>
    <div class="card-content">
      <div class="brand">
        <div class="brand-square"></div>
        <div class="brand-name">Cobalt Wayline</div>
      </div>
      <div class="person-name">Daniel Tan</div>
      <ul class="contact-list">
        <li class="contact-item">
          <svg class="contact-icon" viewBox="0 0 26 26" aria-hidden="true">
            <circle cx="13" cy="13" r="12" fill="#fff"/>
            <path d="M9 7.5c.6-.5 1.4-.4 1.8.2l1.1 1.8c.3.5.2 1.1-.2 1.5l-.8.7c.6 1.5 1.7 2.7 3.1 3.4l.7-.8c.4-.4 1-.5 1.5-.2l1.8 1.1c.6.4.7 1.2.2 1.8l-.8.9c-.6.6-1.5.8-2.3.5-3.2-1.3-5.6-3.8-6.8-7-.3-.8-.1-1.7.5-2.3z" fill="#05070c"/>
          </svg>
          +65 9000-1234
        </li>
        <li class="contact-item">
          <svg class="contact-icon" viewBox="0 0 26 26" aria-hidden="true">
            <circle cx="13" cy="13" r="12" fill="none" stroke="#fff" stroke-width="1.6"/>
            <rect x="6.5" y="8.5" width="13" height="9" fill="none" stroke="#fff" stroke-width="1.5"/>
            <path d="M6.5 8.5l6.5 5 6.5-5" fill="none" stroke="#fff" stroke-width="1.5"/>
          </svg>
          daniel@cobalt-wayline.example
        </li>
        <li class="contact-item">
          <svg class="contact-icon" viewBox="0 0 26 26" aria-hidden="true">
            <circle cx="13" cy="13" r="11" fill="none" stroke="#fff" stroke-width="1.6"/>
            <ellipse cx="13" cy="13" rx="5" ry="11" fill="none" stroke="#fff" stroke-width="1.4"/>
            <line x1="2" y1="13" x2="24" y2="13" stroke="#fff" stroke-width="1.4"/>
            <line x1="4" y1="7.5" x2="22" y2="7.5" stroke="#fff" stroke-width="1.2"/>
            <line x1="4" y1="18.5" x2="22" y2="18.5" stroke="#fff" stroke-width="1.2"/>
          </svg>
          www.cobalt-wayline.example
        </li>
      </ul>
    </div>
  </div>
</body>
</html>
```